Online-Marketing Material für Recruiting-Plattform
Zielgruppe
Recruiting-Plattform für Physiotherapeuten. Wir sind Vermittler.
Aufgabenstellung
Ich benötige ein 2er Set aus Social-Media-Templates, das wir als Basis für Recruiting-Ads nutzen können.
Variante 1: (1080 x 1350) mit jeweils 285 Pixel Safe Space oben und unten (hier keine wichtigen Elemente).
Wichtig: Es handelt sich um ein Template. Daher muss es mit verschiedenen Elementen und Fotos funktionieren.
Die Elemente werden später durch variable Inhalte gesetzt. Ziel ist es, ein möglichst flexibles Format zu schaffen,
das mit unterschiedlichen Inhalten funktioniert.
Bitte orientiere dich am Grunddesign der Website therapunkt.de
Elemente und zugehörige Beispiele sind
1. Foto in querformat | Beispiel als Download)
2. Jobtitel als Headline | (Physiotherapeut (m/w/d)
3. Subtitle | Werde Teil eines wachsenden Teams
4. Arbeitszeitmodell | Vollzeit, Teilzeit
3. Ort | Hannover
4. 3 x Highlights | 1. Betriebliche Krankenversicherung 2. Tretlux 3. Gehalt bis zu 4.500 EUR
(Die Highlight variieren thematisch, daher hier bitte nur mit thematisch-neutralen Icons arbeiten.
5. Logo des Arbeitgebers (lusen) auf weiß
Variante 2 mit Foto in hochformat

```html
<!DOCTYPE html>
<html lang="de">
<head>
<meta charset="utf-8">
<title>Recruiting-Templates – Physiotherapeut</title>
<link href="https://fonts.googleapis.com/css2?family=Montserrat:wght@600;700;800&display=swap" rel="stylesheet">
<style>
  :root {
    --teal: #0a96a2;
    --navy: #003b4b;
    --yellow: #fcc63d;
    --white: #ffffff;
    --stage: #5e5e5e;
    --rule: #c9c9c9;
  }
  * { margin: 0; padding: 0; box-sizing: border-box; }
  html, body { width: 1200px; height: 1117px; overflow: hidden; }
  body { background: var(--stage); font-family: "Montserrat", Arial, sans-serif; position: relative; }

  /* 1080 x 1350 scaled to 530 x 662; safe zones: top 0–140, bottom 522–662 */
  .poster {
    position: absolute; top: 228px; width: 530px; height: 662px;
    background: var(--white); overflow: hidden;
    box-shadow: 0 6px 16px rgba(0,0,0,.35);
  }
  .poster--landscape { left: 62px; }
  .poster--portrait { left: 608px; }

  .corner-blob { position: absolute; left: 0; top: 0; }
  .top-line {
    position: absolute; left: 254px; top: 38px; width: 276px; height: 10px;
    background: linear-gradient(90deg, var(--teal), var(--yellow));
  }
  .side-bar { position: absolute; top: 200px; width: 25px; height: 100px; background: var(--teal); }
  .side-bar--left { left: 0; }
  .side-bar--right { right: 0; }

  .photo { position: absolute; border-radius: 22px; }
  .photo--room {
    left: 32px; top: 150px; width: 466px; height: 200px;
    background: linear-gradient(120deg, #f3e2b8 0%, #fbf1d6 45%, #e9dcc0 70%, #6f6e72 100%);
  }
  .photo--treatment {
    left: 300px; top: 150px; width: 205px; height: 280px;
    background: linear-gradient(160deg, #f4f4f2 0%, #e7e9ee 45%, #7d8aa3 75%, #2f4266 100%);
  }

  .logo-tab {
    position: absolute; left: 0; top: 0; width: 210px; height: 196px;
    background: var(--white); border-bottom-right-radius: 36px;
  }

  .brand {
    position: absolute; left: 34px; top: 148px;
    font-size: 40px; font-weight: 700; color: var(--navy); letter-spacing: -1px; line-height: 1;
    display: flex; align-items: center; gap: 9px;
  }
  .brand-dot { width: 21px; height: 21px; border-radius: 50%; background: var(--teal); }

  .headline { position: absolute; font-weight: 800; color: var(--teal); letter-spacing: -0.8px; line-height: 1.1; }
  .subline { position: absolute; font-weight: 700; color: var(--navy); letter-spacing: -0.4px; }

  .poster--landscape .headline { left: 0; width: 530px; top: 358px; text-align: center; font-size: 34px; }
  .poster--landscape .subline { left: 0; width: 530px; top: 400px; text-align: center; font-size: 18px; }

  .poster--portrait .brand { left: 32px; top: 150px; }
  .poster--portrait .headline { left: 32px; top: 210px; width: 260px; font-size: 29px; }
  .poster--portrait .subline { left: 32px; top: 286px; width: 260px; font-size: 17px; line-height: 1.25; }

  .perk { position: absolute; width: 120px; margin-left: -60px; text-align: center; }
  .perk-icon {
    width: 40px; height: 40px; border-radius: 50%; background: var(--yellow);
    margin: 0 auto; display: flex; align-items: center; justify-content: center;
  }
  .perk-label { margin-top: 8px; font-size: 9.5px; font-weight: 700; color: var(--navy); line-height: 1.15; }
  .perk--bike .perk-label { margin-top: 12px; }
  .perk-divider { position: absolute; width: 2px; height: 30px; background: var(--rule); }

  .poster--landscape .perk { top: 434px; }
  .poster--landscape .perk-divider { top: 437px; }
  .poster--landscape .perk--bike { left: 49px; }
  .poster--landscape .perk--insurance { left: 135px; }
  .poster--landscape .perk--salary { left: 231px; }

  .poster--portrait .perk { top: 444px; }
  .poster--portrait .perk-divider { top: 447px; }
  .poster--portrait .perk--bike { left: 90px; }
  .poster--portrait .perk--insurance { left: 265px; }
  .poster--portrait .perk--salary { left: 440px; }

  .job-facts {
    position: absolute; background: var(--teal); height: 60px;
    padding: 8px 0 0 22px; color: var(--white); font-size: 14px; font-weight: 700;
  }
  .job-fact { display: flex; align-items: center; gap: 10px; height: 22px; }
  .poster--landscape .job-facts { left: 279px; top: 436px; width: 251px; border-radius: 30px 0 0 30px; }
  .poster--portrait .job-facts { left: 0; top: 350px; width: 285px; border-radius: 0 30px 30px 0; padding-left: 32px; }

  .bottom-band {
    position: absolute; left: 0; top: 611px; width: 200px; height: 51px;
    background: linear-gradient(90deg, var(--yellow), var(--teal));
  }
  .bottom-wave { position: absolute; left: 0; top: 0; }
</style>
</head>
<body>

<section class="poster poster--landscape">
  <svg class="corner-blob" width="130" height="150" viewBox="0 0 130 150"><path d="M0 0 H122 C135 30 120 62 82 82 C40 104 12 118 0 148 Z" fill="var(--yellow)"/></svg>
  <div class="top-line"></div>
  <div class="side-bar side-bar--left"></div>
  <div class="side-bar side-bar--right"></div>
  <div class="photo photo--room" role="img" aria-label="Foto im Querformat: heller Behandlungsraum mit Therapieliege, Sideboard und Fenster"></div>
  <div class="logo-tab"></div>
  <div class="brand">lusen <span class="brand-dot"></span></div>

  <h1 class="headline">Physiotherapeut (m/w/d)</h1>
  <p class="subline">Werde Teil eines wachsenden Teams</p>

  <div class="perk perk--bike">
    <div class="perk-icon"><svg width="28" height="18" viewBox="0 0 28 18" fill="none" stroke="var(--navy)" stroke-width="2"><circle cx="6" cy="12" r="5"/><circle cx="22" cy="12" r="5"/><path d="M6 12 L11 4 H19 L22 12 M11 4 L15 12 H6 M17 2 H20"/></svg></div>
    <div class="perk-label">Tretlux</div>
  </div>
  <div class="perk-divider" style="left:94px"></div>
  <div class="perk perk--insurance">
    <div class="perk-icon"><svg width="24" height="24" viewBox="0 0 24 24" fill="none" stroke="var(--navy)" stroke-width="1.6"><path d="M4 2 H14 L18 6 V21 H4 Z"/><path d="M11 6 V12 M8 9 H14 M7 15 H12 M7 18 H12"/><path d="M17 13 L22 15 V18 C22 20 19.5 22 17 23 C14.5 22 12 20 12 18 V15 Z" fill="var(--yellow)"/></svg></div>
    <div class="perk-label">Betriebliche<br>Krankenversicherung</div>
  </div>
  <div class="perk-divider" style="left:185px"></div>
  <div class="perk perk--salary">
    <div class="perk-icon"><svg width="24" height="22" viewBox="0 0 24 22" fill="none" stroke="var(--navy)" stroke-width="1.6"><path d="M2 8 L12 3 L22 8 L12 13 Z"/><path d="M2 12 L12 17 L22 12 M2 16 L12 21 L22 16"/><circle cx="12" cy="8" r="1.8"/></svg></div>
    <div class="perk-label">Gehalt bis zu<br>4.500 EUR</div>
  </div>

  <div class="job-facts">
    <div class="job-fact"><svg width="15" height="15" viewBox="0 0 16 16" fill="none" stroke="var(--white)" stroke-width="1.5"><circle cx="8" cy="8" r="7"/><path d="M8 4 V8 L10.5 10"/></svg>Vollzeit | Teilzeit</div>
    <div class="job-fact"><svg width="15" height="16" viewBox="0 0 16 18" fill="none" stroke="var(--white)" stroke-width="1.5"><path d="M8 17 C3 11 2 9 2 7 A6 6 0 0 1 14 7 C14 9 13 11 8 17 Z"/><circle cx="8" cy="7" r="2.2"/></svg>Standort bei Hannover</div>
  </div>

  <div class="bottom-band"></div>
  <svg class="bottom-wave" width="530" height="662" viewBox="0 0 530 662"><path d="M157 662 C155 610 195 566 262 575 C325 584 360 650 430 648 C480 646 508 622 530 602 V662 Z" fill="var(--navy)"/></svg>
</section>

<section class="poster poster--portrait">
  <svg class="corner-blob" width="130" height="150" viewBox="0 0 130 150"><path d="M0 0 H122 C135 30 120 62 82 82 C40 104 12 118 0 148 Z" fill="var(--yellow)"/></svg>
  <div class="top-line"></div>
  <div class="side-bar side-bar--right"></div>
  <div class="photo photo--treatment" role="img" aria-label="Foto im Hochformat: Physiotherapeutin dehnt das Bein eines liegenden Patienten auf einer Therapieliege"></div>
  <div class="brand">lusen <span class="brand-dot"></span></div>

  <h1 class="headline">Physiotherapeut<br>(m/w/d)</h1>
  <p class="subline">Werde Teil eines<br>wachsenden Teams</p>

  <div class="job-facts">
    <div class="job-fact"><svg width="15" height="15" viewBox="0 0 16 16" fill="none" stroke="var(--white)" stroke-width="1.5"><circle cx="8" cy="8" r="7"/><path d="M8 4 V8 L10.5 10"/></svg>Vollzeit | Teilzeit</div>
    <div class="job-fact"><svg width="15" height="16" viewBox="0 0 16 18" fill="none" stroke="var(--white)" stroke-width="1.5"><path d="M8 17 C3 11 2 9 2 7 A6 6 0 0 1 14 7 C14 9 13 11 8 17 Z"/><circle cx="8" cy="7" r="2.2"/></svg>Standort bei Hannover</div>
  </div>

  <div class="perk perk--bike">
    <div class="perk-icon"><svg width="28" height="18" viewBox="0 0 28 18" fill="none" stroke="var(--navy)" stroke-width="2"><circle cx="6" cy="12" r="5"/><circle cx="22" cy="12" r="5"/><path d="M6 12 L11 4 H19 L22 12 M11 4 L15 12 H6 M17 2 H20"/></svg></div>
    <div class="perk-label">Tretlux</div>
  </div>
  <div class="perk-divider" style="left:177px"></div>
  <div class="perk perk--insurance">
    <div class="perk-icon"><svg width="24" height="24" viewBox="0 0 24 24" fill="none" stroke="var(--navy)" stroke-width="1.6"><path d="M4 2 H14 L18 6 V21 H4 Z"/><path d="M11 6 V12 M8 9 H14 M7 15 H12 M7 18 H12"/><path d="M17 13 L22 15 V18 C22 20 19.5 22 17 23 C14.5 22 12 20 12 18 V15 Z" fill="var(--yellow)"/></svg></div>
    <div class="perk-label">Betriebliche<br>Krankenversicherung</div>
  </div>
  <div class="perk-divider" style="left:352px"></div>
  <div class="perk perk--salary">
    <div class="perk-icon"><svg width="24" height="22" viewBox="0 0 24 22" fill="none" stroke="var(--navy)" stroke-width="1.6"><path d="M2 8 L12 3 L22 8 L12 13 Z"/><path d="M2 12 L12 17 L22 12 M2 16 L12 21 L22 16"/><circle cx="12" cy="8" r="1.8"/></svg></div>
    <div class="perk-label">Gehalt bis zu<br>4.500 EUR</div>
  </div>

  <div class="bottom-band"></div>
  <svg class="bottom-wave" width="530" height="662" viewBox="0 0 530 662"><path d="M157 662 C155 610 195 566 262 575 C325 584 360 650 430 648 C480 646 508 622 530 602 V662 Z" fill="var(--navy)"/></svg>
</section>

</body>
</html>
```